Hardwood Flooring Company needs packaging design

We need a packaging design for our new product. We manufacture wood flooring and this year we are launching a new product that is high quality and superior durability and we want a design that communicate the superior quality of our product. We would like to see a nice design with colors shapes that communicates quality and fashion. The product carries warranty, so we need something like a 30 year warranty stamp on the box. Measurements of the box are 4” high (100mm) X 10” wide (250mm) x 84” long (2100mm).

Industry/Entity Type

Flooring

Requirements
Must have
• 30 Year warranty stamp
Should not have
• colors like blue or purple

```html
<!DOCTYPE html>
<html lang="en">
<head>
<meta charset="utf-8">
<title>Veronda Flooring Box – Dieline Layout</title>
<link href="https://fonts.googleapis.com/css2?family=Montserrat:wght@400;500;700&display=swap" rel="stylesheet">
<style>
  :root {
    --paper: #ffffff;
    --kraft: #c8baa6;
    --rust: #c0622f;
    --charcoal: #3f3834;
    --ink: #222222;
    --gold-light: #b9a67a;
    --gold-dark: #8a7a52;
    --silver-light: #e4e0d8;
    --silver-dark: #9c968a;
    --edge: #8c8378;
  }
  * { margin: 0; padding: 0; box-sizing: border-box; }
  html, body { width: 1200px; height: 848px; overflow: hidden; background: var(--paper); }
  body { font-family: "Montserrat", Arial, sans-serif; color: var(--ink); }
  .sheet { position: relative; width: 1200px; height: 848px; }

  .panel { position: absolute; left: 150px; width: 893px; }
  .panel-label { position: absolute; left: 150px; font-size: 9px; letter-spacing: 0.5px; color: var(--ink); }

  .brand-name {
    position: absolute; font-family: "Montserrat", Arial, sans-serif;
    font-weight: 700; color: var(--rust); line-height: 1; white-space: nowrap;
  }

  /* back */
  .panel-back { top: 105px; height: 106px; background: var(--kraft); }
  .panel-back .band { position: absolute; left: 0; top: 0; width: 100%; height: 37px; background: var(--rust); }
  .panel-back .brand-name { right: 14px; top: 60px; font-size: 40px; letter-spacing: 2px; }

  /* top */
  .panel-top { top: 251px; height: 42px; background: var(--charcoal); }

  /* front */
  .panel-front { top: 329px; height: 108px; background: var(--kraft); border: 1px solid var(--edge); }
  .panel-front .brand-name { left: 12px; top: 10px; font-size: 40px; letter-spacing: 2px; }
  .panel-front .product-line { position: absolute; left: 13px; top: 51px; font-size: 11px; color: var(--rust); letter-spacing: 0.2px; }
  .panel-front .band { position: absolute; left: 0; top: 77px; width: 100%; height: 30px; background: var(--rust); }
  .panel-front .tagline { position: absolute; left: 13px; top: 85px; font-size: 11px; color: #fff; letter-spacing: 0.5px; }
  .panel-front .seal { position: absolute; left: 792px; top: 4px; width: 96px; height: 96px; }

  /* end flaps */
  .flap { position: absolute; top: 329px; width: 43px; height: 108px; background: var(--kraft); }
  .flap-left { left: 80px; }
  .flap-right { left: 1066px; }
  .flap svg { position: absolute; left: 0; top: 0; }
  .flap .brand-name {
    font-size: 9px; letter-spacing: 0.5px; top: 54px; left: 22px;
    transform: translate(-50%, -50%) rotate(90deg);
  }

  /* bottom */
  .panel-bottom { top: 468px; height: 43px; background: var(--rust); border: 1px solid var(--edge); }
  .panel-bottom .brand-name { left: 633px; top: 5px; font-size: 15px; color: #fff; letter-spacing: 1px; }
  .panel-bottom .spec-bar { position: absolute; left: 736px; top: 5px; width: 156px; height: 11px; background: #fff; }
  .panel-bottom .specs { position: absolute; left: 736px; top: 20px; font-size: 6.5px; color: #fff; line-height: 1.2; }
  .panel-bottom .specs .qty { font-size: 5.5px; }

  /* seal reference */
  .seal-sample { position: absolute; left: 86px; top: 624px; width: 124px; height: 124px; }
  .seal-caption { position: absolute; left: 28px; top: 762px; width: 240px; text-align: center; font-size: 9px; line-height: 16px; letter-spacing: 0.2px; }

  .sheet-brand { position: absolute; left: 945px; top: 783px; font-size: 25px; letter-spacing: 1.5px; }
</style>
</head>
<body>
<main class="sheet">

  <section class="panel panel-back">
    <div class="band"></div>
    <span class="brand-name">VERONDA</span>
  </section>
  <p class="panel-label" style="top:221px">BACK</p>

  <section class="panel panel-top"></section>
  <p class="panel-label" style="top:305px">TOP</p>

  <aside class="flap flap-left">
    <svg width="43" height="108" viewBox="0 0 43 108">
      <rect x="0.5" y="0.5" width="42" height="107" fill="none" stroke="#8c8378"/>
      <polyline points="0,0 43,16 43,92 0,108" fill="none" stroke="#8c8378" stroke-width="0.8"/>
    </svg>
    <span class="brand-name">VERONDA</span>
  </aside>

  <section class="panel panel-front">
    <span class="brand-name">VERONDA</span>
    <p class="product-line">WOOD FLOORING TILES (MAPLE WOOD FINISH)</p>
    <div class="band"></div>
    <p class="tagline">STRONG &amp; DURABLE</p>
    <svg class="seal" viewBox="0 0 100 100" role="img" aria-label="30 year warranty seal in silver foil">
      <defs>
        <radialGradient id="foil" cx="40%" cy="35%" r="70%">
          <stop offset="0" stop-color="var(--silver-light)"/>
          <stop offset="1" stop-color="var(--silver-dark)"/>
        </radialGradient>
      </defs>
      <circle cx="50" cy="50" r="46" fill="url(#foil)"/>
    </svg>
  </section>
  <p class="panel-label" style="top:445px">FRONT</p>

  <aside class="flap flap-right">
    <svg width="43" height="108" viewBox="0 0 43 108">
      <rect x="0.5" y="0.5" width="42" height="107" fill="none" stroke="#8c8378"/>
      <polyline points="43,0 0,16 0,92 43,108" fill="none" stroke="#8c8378" stroke-width="0.8"/>
    </svg>
    <span class="brand-name">VERONDA</span>
  </aside>

  <section class="panel panel-bottom">
    <span class="brand-name">VERONDA</span>
    <div class="spec-bar"></div>
    <p class="specs">SPECS: 84" x 10" x 3/4"<br><span class="qty">QTY: 10 PCS</span></p>
  </section>
  <p class="panel-label" style="top:529px">BOTTOM</p>

  <svg class="seal-sample" viewBox="0 0 100 100" role="img" aria-label="30 year warranty seal in gold foil">
    <defs>
      <radialGradient id="gold" cx="40%" cy="35%" r="70%">
        <stop offset="0" stop-color="var(--gold-light)"/>
        <stop offset="1" stop-color="var(--gold-dark)"/>
      </radialGradient>
    </defs>
    <circle cx="50" cy="50" r="48" fill="url(#gold)"/>
  </svg>
  <p class="seal-caption">WARRANTY SEAL OF EXCELLENCE &amp; QUALITY<br>SHINY GOLDFOIL TYPE</p>

  <span class="brand-name sheet-brand">VERONDA</span>
</main>
</body>
</html>
```